Pelton Mortgage Capital Business Card

We need a business card design for our mortgage servicing company. In addition to servicing the loans of homeowners, we help homeowners with purchasing their homes and any mortgage refinancing. We would like to see designs that use the colors in the logo attached below (gold-ish yellow and navy blue), and any other design you deem fit! The design should communicate a simpler life with smart mortgages provided by Pelton.

```html
<!DOCTYPE html>
<html lang="en">
<head>
<meta charset="utf-8">
<title>Pelton Mortgage Capital Business Card</title>
<link rel="stylesheet" href="https://fonts.googleapis.com/css2?family=Open+Sans:wght@400;600;700&display=swap">
<style>
  :root {
    --backdrop: #222223;
    --gold: #e1b141;
    --navy: #1f1a5c;
    --card-dark: #212024;
    --white: #ffffff;
  }
  * { box-sizing: border-box; margin: 0; padding: 0; }
  html, body {
    width: 1200px;
    height: 780px;
    overflow: hidden;
    background: var(--backdrop);
    font-family: "Open Sans", Arial, sans-serif;
  }
  .canvas { position: relative; width: 1200px; height: 780px; }

  .card {
    position: absolute;
    width: 520px;
    height: 297px;
    box-shadow: 0 10px 24px rgba(0, 0, 0, 0.55);
  }

  /* Front */
  .card-front {
    left: 70px;
    top: 90px;
    background: var(--gold);
    display: flex;
    align-items: center;
    justify-content: center;
  }
  .brand {
    display: flex;
    align-items: center;
    gap: 14px;
  }
  .brand-mark {
    width: 22px;
    height: 22px;
    border-radius: 50%;
  }
  .brand-name {
    font-weight: 700;
    letter-spacing: 0.5px;
  }
  .card-front .brand-mark { background: var(--navy); }
  .card-front .brand-name { color: var(--navy); font-size: 46px; }

  /* Back */
  .card-back {
    left: 610px;
    top: 390px;
    background: var(--card-dark);
    border-bottom: 4px solid var(--gold);
  }
  .card-back .brand {
    position: absolute;
    right: 36px;
    top: 42px;
  }
  .card-back .brand-mark { width: 14px; height: 14px; background: var(--gold); }
  .card-back .brand-name { color: var(--gold); font-size: 28px; }

  .details {
    position: absolute;
    left: 0;
    bottom: 26px;
    padding-left: 34px;
    color: var(--white);
  }
  .accent-bar {
    position: absolute;
    left: 0;
    top: 4px;
    width: 24px;
    height: 44px;
    background: var(--gold);
  }
  .person-name {
    font-size: 27px;
    font-weight: 700;
    line-height: 1.05;
  }
  .person-name .first { color: var(--gold); }
  .person-name .last { color: var(--white); }
  .person-role {
    font-size: 14px;
    font-weight: 600;
    margin-top: 2px;
  }
  .address {
    font-size: 13.5px;
    line-height: 1.35;
    margin-top: 12px;
    padding-left: 14px;
    font-style: normal;
  }
  .contacts {
    list-style: none;
    margin-top: 10px;
    padding-left: 14px;
  }
  .contacts li {
    display: flex;
    align-items: center;
    gap: 9px;
    font-size: 13.5px;
    line-height: 1.45;
  }
  .contacts svg { width: 13px; height: 13px; flex: none; }
  .contacts svg * { fill: none; stroke: var(--gold); stroke-width: 2; }
</style>
</head>
<body>
<main class="canvas">
  <section class="card card-front" aria-label="Card front">
    <div class="brand">
      <span class="brand-mark"></span>
      <span class="brand-name">Pelton Mortgage</span>
    </div>
  </section>

  <section class="card card-back" aria-label="Card back">
    <div class="brand">
      <span class="brand-mark"></span>
      <span class="brand-name">Pelton Mortgage</span>
    </div>

    <div class="details">
      <span class="accent-bar"></span>
      <h1 class="person-name"><span class="first">Lena</span> <span class="last">Varga</span></h1>
      <p class="person-role">Managing Director</p>
      <address class="address">418 Harlow Ave. Suite 120<br>Denton, TX 76201</address>
      <ul class="contacts">
        <li>
          <svg viewBox="0 0 24 24" aria-hidden="true"><path d="M5 3h4l2 5-2.5 1.5a11 11 0 0 0 6 6L16 13l5 2v4a2 2 0 0 1-2 2A16 16 0 0 1 3 5a2 2 0 0 1 2-2z"/></svg>
          (555) 214-3609
        </li>
        <li>
          <svg viewBox="0 0 24 24" aria-hidden="true"><rect x="3" y="5" width="18" height="14" rx="1"/><path d="M3 6l9 7 9-7"/></svg>
          info@website.com
        </li>
        <li>
          <svg viewBox="0 0 24 24" aria-hidden="true"><circle cx="12" cy="12" r="9"/><path d="M3 12h18M12 3c3 3 3 15 0 18M12 3c-3 3-3 15 0 18"/></svg>
          www.website.com
        </li>
      </ul>
    </div>
  </section>
</main>
</body>
</html>
```